Roofing Contractor business card redesign

I want to redesign my business card with a fresh, eye catching concept

Target Market(s)

Residential Roofing Clients, potential employees, and subcontractors.

Industry/Entity Type

Business

Colors

Designer to choose colors to be used in the design.

Requirements
Nice to have
• I just want something that's more pleasing to the eye. You can use a combination of either / or of my logos.

```html
<!DOCTYPE html>
<html lang="en">
<head>
<meta charset="utf-8">
<title>Bright Roof General Contractors – Business Card</title>
<link href="https://fonts.googleapis.com/css2?family=Source+Sans+3:wght@400;600;700;800&display=swap" rel="stylesheet">
<style>
  :root {
    --backdrop: #2f2825;
    --card: #fbfbfa;
    --brand-dark: #4a1410;
    --brand-red: #6e1712;
    --ink: #2b2b2b;
    --mark: #e9a63a;
  }
  html, body {
    margin: 0;
    width: 1200px;
    height: 844px;
    overflow: hidden;
    background: var(--backdrop);
    font-family: "Source Sans 3", sans-serif;
  }
  .stage {
    position: relative;
    width: 1200px;
    height: 844px;
  }
  .card {
    position: absolute;
    top: 279px;
    width: 500px;
    height: 286px;
    background: var(--card);
    box-shadow: 0 8px 24px rgba(0,0,0,.45);
    box-sizing: border-box;
  }
  .card--front { left: 60px; }
  .card--back  { left: 640px; }

  .brand {
    display: flex;
    flex-direction: column;
    align-items: center;
    color: var(--brand-dark);
    font-weight: 800;
  }
  .brand__name {
    display: flex;
    align-items: center;
    gap: 8px;
    font-size: 46px;
    line-height: 1;
    letter-spacing: -1px;
  }
  .brand__dot {
    width: 40px;
    height: 40px;
    border-radius: 50%;
    background: var(--mark);
    flex: none;
  }
  .brand__tagline {
    font-size: 21px;
    line-height: 1.1;
    margin-top: 2px;
  }
  .card--front .brand {
    position: absolute;
    left: 70px;
    top: 30px;
  }
  .card--back .brand {
    position: absolute;
    left: 0;
    right: 0;
    top: 100px;
  }

  .person {
    position: absolute;
    left: 38px;
    top: 150px;
    color: var(--ink);
    font-size: 15px;
    line-height: 1.3;
  }
  .person__name {
    color: var(--brand-red);
    font-weight: 600;
    font-size: 19px;
  }
  .person__address { margin-top: 12px; }

  .contact {
    position: absolute;
    right: 26px;
    top: 110px;
    margin: 0;
    padding: 0;
    list-style: none;
    color: var(--ink);
    font-size: 14px;
    line-height: 1.5;
    text-align: right;
  }
  .contact li {
    display: flex;
    justify-content: flex-end;
    align-items: center;
    gap: 8px;
  }
  .contact svg {
    width: 11px;
    height: 11px;
    fill: var(--brand-dark);
    stroke: var(--brand-dark);
  }
</style>
</head>
<body>
<main class="stage">
  <section class="card card--front" aria-label="Business card front">
    <div class="brand">
      <div class="brand__name">Bright <span class="brand__dot"></span> Roof</div>
      <div class="brand__tagline">General Contractors, Inc.</div>
    </div>

    <div class="person">
      <div class="person__name">Sam Whitlow</div>
      <div>Harlow Certified Roof Inspector</div>
      <div>Licensed Property Adjuster</div>
      <div class="person__address">4180 Maple Ridge Road Suite 110<br>Fairview, TX 75069</div>
    </div>

    <ul class="contact">
      <li>(555) 014-2000
        <svg viewBox="0 0 12 12" aria-hidden="true"><path stroke="none" d="M2 1l2 0 1 3-1.5 1a6 6 0 0 0 3.5 3.5L8 7l3 1v2a1 1 0 0 1-1 1A9 9 0 0 1 1 2a1 1 0 0 1 1-1z"/></svg>
      </li>
      <li>(555) 016-7731
        <svg viewBox="0 0 12 12" aria-hidden="true"><rect x="3" y="0.5" width="6" height="11" rx="1" fill="none" stroke-width="1.2"/><circle cx="6" cy="9.5" r=".7" stroke="none"/></svg>
      </li>
      <li>sam@brightrooftx.com
        <svg viewBox="0 0 12 12" aria-hidden="true"><rect x="0.5" y="2" width="11" height="8" stroke="none"/><path d="M1 2.5l5 4 5-4" fill="none" stroke="#fff" stroke-width="1"/></svg>
      </li>
      <li>BrightRoofGC.com
        <svg viewBox="0 0 12 12" aria-hidden="true"><circle cx="6" cy="6" r="5.5" stroke="none"/><path d="M.5 6h11M6 .5c-3 3-3 8 0 11M6 .5c3 3 3 8 0 11" fill="none" stroke="#fff" stroke-width=".8"/></svg>
      </li>
    </ul>
  </section>

  <section class="card card--back" aria-label="Business card back">
    <div class="brand">
      <div class="brand__name">Bright <span class="brand__dot"></span> Roof</div>
      <div class="brand__tagline">General Contractors, Inc.</div>
    </div>
  </section>
</main>
</body>
</html>
```